New Record Label needs a Web design

We are Moss Lantern: a London based, new & independent music production company aimed at the 25-40 age group. The musical style is Soul/Classic Motown.
We have at the moment just one signed artist, but will expand in the future.
We dont' have any webpage yet and are looking for an innovative web design for our webpage www.moss-lantern.com
I have uploaded our company logo.

Initially the whole website will only have 3 tabs: Home page/Artists/Contact

The design should be classic and high-end, but can be a bit crazy too.

```html
<!DOCTYPE html>
<html lang="en">
<head>
<meta charset="utf-8">
<title>Moss Lantern – Soul &amp; Classic Records</title>
<link rel="stylesheet" href="https://fonts.googleapis.com/css2?family=Open+Sans:wght@400;600;700&display=swap">
<style>
:root{
  --page:#ffffff;
  --charcoal:#1e1e1e;
  --black:#050505;
  --nav-active:#0c0c0c;
  --divider:#2c2c2c;
  --slate:#4a4a4a;
  --red:#e8363b;
  --orange:#f26a35;
  --orange-dark:#e0552a;
  --text-dark:#333333;
  --text-body:#3c3c3c;
  --white:#ffffff;
  --muted:#bdbdbd;
}
*{margin:0;padding:0;box-sizing:border-box}
html,body{width:845px;height:1200px;overflow:hidden;background:var(--page)}
body{font-family:"Open Sans",Arial,sans-serif;color:var(--text-body);position:relative}
.site{position:absolute;left:11px;top:11px;width:820px;height:1172px}
.abs{position:absolute}

/* header */
.site-header{left:0;top:0;width:820px;height:69px;background:var(--charcoal);border-bottom:2px solid var(--red)}
.brand{left:127px;top:0;height:67px;display:flex;align-items:center;gap:10px;color:var(--red);font-size:26px;font-weight:600;letter-spacing:.2px}
.brand-dot{width:22px;height:22px;border-radius:50%;background:var(--red)}
.main-nav{left:454px;top:0;height:67px;display:flex}
.nav-item{height:67px;display:flex;align-items:center;gap:6px;padding:0 12px;color:var(--white);font-size:10.5px;font-weight:600;text-transform:uppercase;border-right:1px solid var(--divider)}
.nav-item.is-active{background:var(--nav-active);font-weight:700}
.nav-item svg{width:12px;height:12px}

/* hero */
.hero{left:0;top:69px;width:820px;height:237px;background:radial-gradient(ellipse at 55% 45%,#8a8a8a 0%,#4a4a4a 30%,#1a1a1a 60%,#050505 100%)}
.hero-title{left:0;top:124px;width:820px;text-align:center;color:var(--white);font-size:22px;font-weight:700;letter-spacing:.3px;text-shadow:0 2px 4px rgba(0,0,0,.7)}
.hero-arrow{top:100px;width:26px;height:22px}
.hero-dots{left:391px;top:218px;display:flex;gap:3px}
.hero-dots span{width:10px;height:10px;border-radius:50%;border:1.5px solid var(--white)}
.hero-dots span.is-current{background:var(--red)}

/* player */
.player{left:0;top:306px;width:820px;height:75px;background:var(--slate);border-top:2px solid #2a2a2a}
.player-title{left:0;top:11px;width:820px;text-align:center;color:var(--white);font-size:14.5px;font-weight:600}
.player-controls{left:136px;top:40px;display:flex;gap:4px;align-items:center}
.player-bar{left:212px;top:40px;width:468px;height:22px;background:var(--white);border-radius:2px;font-size:7px;color:#999}
.track{left:38px;top:10px;width:262px;height:2px;background:#cfcfcf}
.track i,.volume i{position:absolute;left:0;top:0;height:2px;background:var(--orange)}
.volume-box{left:336px;top:1px;width:94px;height:20px;background:#ececec}
.volume{left:20px;top:9px;width:56px;height:2px;background:#cfcfcf}

/* intro */
.intro{left:0;top:381px;width:820px;height:226px;background:var(--page)}
.intro h1{position:absolute;left:0;top:15px;width:820px;text-align:center;font-size:18px;font-weight:600;color:var(--text-dark)}
.intro h1 em{font-style:normal;color:var(--red)}
.intro p{position:absolute;left:127px;width:570px;font-size:11.2px;line-height:18px;color:var(--text-body)}

/* artists */
.artists{left:0;top:607px;width:820px;height:307px;background:var(--charcoal)}
.section-title{left:0;top:14px;width:820px;text-align:center;color:var(--white);font-size:14.5px;font-weight:600}
.artist{top:52px;width:130px;text-align:center;color:var(--white);font-size:11.5px;font-weight:600}
.artist-photo{display:block;margin:0 auto 12px;width:126px;height:126px;border-radius:50%;border:3px solid var(--white);box-shadow:0 4px 8px rgba(0,0,0,.6)}
.artist.is-featured .artist-photo{border-color:var(--red)}
.artists-arrow{top:112px;width:20px;height:18px}
.btn-view{left:341px;top:236px;width:138px;height:31px;background:linear-gradient(var(--orange),var(--orange-dark));color:var(--white);font-size:12px;font-weight:600;display:flex;align-items:center;justify-content:center;gap:7px}

/* footer */
.footer{left:0;top:914px;width:820px;height:158px;background:var(--charcoal);border-top:2px solid var(--red)}
.footer-col{top:30px;color:var(--white)}
.footer-col h3{font-size:11.5px;font-weight:600;display:flex;align-items:center;gap:5px;margin-bottom:8px}
.footer-col h3 svg{width:11px;height:11px}
.link-list{list-style:none;width:100px;margin-left:7px}
.link-list li{font-size:9.5px;padding:3px 0 5px 6px;border-bottom:1px solid #3a3a3a;color:var(--white)}
.link-list li.is-active{color:var(--red);font-weight:700}
.tweet{margin-left:17px;font-size:8.5px;line-height:13px}
.tweet a{color:var(--red);text-decoration:none;display:block}
.tweet time{display:block;font-size:7.5px;margin-top:9px}
.photo-grid{display:grid;grid-template-columns:repeat(3,36px);gap:3px 4px}
.photo-grid span{height:33px;background:linear-gradient(135deg,#6a5a5a,#2a2228)}
.photo-grid span:nth-child(3),.photo-grid span:nth-child(6){background:linear-gradient(135deg,#b03a4a,#4a2050)}
.photo-grid span:nth-child(5){background:linear-gradient(135deg,#2a4aa0,#1a1a40)}
.email-field{width:137px;height:19px;background:#141414;color:#555;font-size:7.5px;padding:5px 5px}
.socials{margin-top:20px;display:flex;gap:6px}
.socials span{width:19px;height:19px;border-radius:50%;background:#5a5a5a}
.btn-submit{left:80px;top:82px;width:57px;height:24px;background:var(--red);color:var(--white);font-size:11px;font-weight:700;display:flex;align-items:center;justify-content:center}

/* contact band */
.contact-band{left:0;top:1072px;width:820px;height:65px;background:var(--black);color:var(--white)}
.contact-band h2{position:absolute;left:0;top:9px;width:820px;text-align:center;color:var(--red);font-size:17px;font-weight:400}
.contact-line{left:0;top:39px;width:820px;display:flex;justify-content:center;align-items:center;gap:8px;font-size:11px}
.contact-line svg{width:11px;height:12px}

/* legal */
.legal{left:0;top:1137px;width:820px;height:35px;background:var(--charcoal);color:var(--white);font-size:7.5px}
.legal-copy{left:127px;top:13px}
.legal-links{right:126px;top:13px}
</style>
</head>
<body>
<div class="site">

  <header class="site-header abs">
    <div class="brand abs"><span class="brand-dot"></span>Moss Lantern</div>
    <nav class="main-nav abs">
      <span class="nav-item is-active"><svg viewBox="0 0 12 12"><path d="M6 1 L11 6 H9.5 V11 H7 V8 H5 V11 H2.5 V6 H1 Z" fill="#e8363b"/></svg>Home</span>
      <span class="nav-item" style="padding:0 15px 0 20px"><svg viewBox="0 0 12 12" fill="#fff"><circle cx="4" cy="4" r="2"/><circle cx="8.5" cy="4.5" r="1.7"/><path d="M0.5 10c0-3 7-3 7 0z"/><path d="M6.5 8c1-2 5-1.5 5 1.5H8z"/></svg>Artists</span>
      <span class="nav-item" style="padding:0 22px 0 12px"><svg viewBox="0 0 12 12" fill="#fff"><ellipse cx="5" cy="4.5" rx="4.5" ry="3.3"/><path d="M2 7 L1.5 10 L4.5 7.5z"/><ellipse cx="8" cy="7.5" rx="3.5" ry="2.6" opacity=".85"/></svg>Contact</span>
    </nav>
  </header>

  <section class="hero abs" role="img" aria-label="Black and white close-up photograph of an electric guitar body with strings and pickups">
    <svg class="hero-arrow abs" style="left:21px" viewBox="0 0 26 22"><path d="M0 11 L11 0 V7 H26 V15 H11 V22 Z" fill="#fff"/></svg>
    <svg class="hero-arrow abs" style="left:779px" viewBox="0 0 26 22"><path d="M26 11 L15 0 V7 H0 V15 H15 V22 Z" fill="#fff"/></svg>
    <div class="hero-title abs">I LOVE SOUL/CLASSIC MUSIC</div>
    <div class="hero-dots abs"><span class="is-current"></span><span></span><span></span></div>
  </section>

  <section class="player abs">
    <div class="player-title abs">Our New Classic Out</div>
    <div class="player-controls abs">
      <svg width="18" height="18" viewBox="0 0 18 18"><circle cx="9" cy="9" r="8" fill="none" stroke="#fff" stroke-width="1.5"/><path d="M9 6 L5.5 9 L9 12Z M12.5 6 L9 9 L12.5 12Z" fill="#fff"/></svg>
      <svg width="22" height="22" viewBox="0 0 22 22"><circle cx="11" cy="11" r="10" fill="none" stroke="#fff" stroke-width="1.5"/><path d="M8.5 6.5 L15.5 11 L8.5 15.5Z" fill="#fff"/></svg>
      <svg width="18" height="18" viewBox="0 0 18 18"><circle cx="9" cy="9" r="8" fill="none" stroke="#fff" stroke-width="1.5"/><path d="M9 6 L12.5 9 L9 12Z M5.5 6 L9 9 L5.5 12Z" fill="#fff"/></svg>
    </div>
    <div class="player-bar abs">
      <span class="abs" style="left:10px;top:7px">00:02</span>
      <div class="track abs"><i style="width:44px"></i></div>
      <span class="abs" style="left:309px;top:7px">00:15</span>
      <div class="volume-box abs">
        <svg class="abs" style="left:9px;top:6px" width="8" height="8" viewBox="0 0 8 8"><path d="M0 2.5H2L5 0V8L2 5.5H0Z" fill="#555"/></svg>
        <div class="volume abs"><i style="width:46px"></i></div>
        <svg class="abs" style="left:80px;top:6px" width="8" height="8" viewBox="0 0 8 8"><path d="M0 2.5H2L5 0V8L2 5.5H0Z" fill="#555"/></svg>
      </div>
      <svg class="abs" style="left:445px;top:8px" width="7" height="6" viewBox="0 0 7 6" fill="#555"><rect width="7" height="1.2"/><rect y="2.4" width="7" height="1.2"/><rect y="4.8" width="7" height="1.2"/></svg>
    </div>
  </section>

  <section class="intro abs">
    <h1>Hello we’re <em>Moss Lantern</em></h1>
    <p style="top:46px">In elementum pellentesque dolor ac gravida. Pellentesque elit leo, accumsan sed consectetur a, semper ac sem. Morbi sodales bibendum risus nec laoreet. Mauris est nisi, consequat vitae porta et, hendrerit sed metus. Aliquam eu magna vel metus ultrices ornare in et nisi. Quisque porta sodales orci, eu auctor leo tincidunt nec. Suspendisse posuere blandit tortor sit amet varius. Integer condimentum rutrum mi quis lobortis. Etiam consectetur posuere pretium.</p>
    <p style="top:155px">Aliquam eu magna vel metus ultrices ornare in et nisi. Quisque porta sodales orci, eu auctor leo tincidunt nec. Suspendisse posuere blandit tortor sit amet varius. Integer condimentum rutrum mi quis lobortis. Etiam consectetur posuere pretium.</p>
  </section>

  <section class="artists abs">
    <h2 class="section-title abs">Future Artists</h2>
    <svg class="artists-arrow abs" style="left:137px" viewBox="0 0 20 18"><path d="M0 9 L9 0 V6 H20 V12 H9 V18Z" fill="#fff"/></svg>
    <svg class="artists-arrow abs" style="left:665px" viewBox="0 0 20 18"><path d="M20 9 L11 0 V6 H0 V12 H11 V18Z" fill="#fff"/></svg>
    <div class="artist is-featured abs" style="left:169px">
      <span class="artist-photo" role="img" aria-label="Portrait photo of artist Owen Hartley wearing a beanie and headphones" style="background:radial-gradient(circle at 50% 45%,#d8c2b0,#6a6060 55%,#e8e8e8 56%)"></span>Owen Hartley
    </div>
    <div class="artist abs" style="left:345px">
      <span class="artist-photo" role="img" aria-label="Stage photo of singer Rosa Delaine performing at a microphone" style="background:radial-gradient(circle at 50% 55%,#3a2030,#7a30a0 60%,#b040c0)"></span>Rosa Delaine
    </div>
    <div class="artist abs" style="left:521px">
      <span class="artist-photo" role="img" aria-label="Stage photo of singer Marcus Bell performing under pink lights" style="background:radial-gradient(circle at 50% 55%,#4a3050,#a03060 60%,#d04070)"></span>Marcus Bell
    </div>
    <div class="btn-view abs">
      <svg width="18" height="14" viewBox="0 0 18 14" fill="#fff"><circle cx="9" cy="3.5" r="3"/><circle cx="3.5" cy="5" r="2.2"/><circle cx="14.5" cy="5" r="2.2"/><path d="M3.5 14c0-5 11-5 11 0z"/><path d="M0 12c0-3.5 4-4 5-3L3 12z"/><path d="M18 12c0-3.5-4-4-5-3l2 3z"/></svg>
      View All Artists
    </div>
  </section>

  <footer class="footer abs">
    <div class="footer-col abs" style="left:134px">
      <h3><svg viewBox="0 0 11 11" fill="#e8363b"><rect x="4" y="0" width="3" height="3"/><rect x="0" y="7" width="3" height="3"/><rect x="4" y="7" width="3" height="3"/><rect x="8" y="7" width="3" height="3"/><path d="M5.2 3h.6v2H10v2h-.6V5.6H1.6V7H1V5h4.2z"/></svg>Browse Around</h3>
      <ul class="link-list">
        <li class="is-active">Home</li>
        <li>Artists</li>
        <li>Contact</li>
      </ul>
    </div>
    <div class="footer-col abs" style="left:269px">
      <h3><svg viewBox="0 0 11 11"><rect x="1" y="1" width="9" height="9" fill="#e8363b"/></svg>Chirp Feed</h3>
      <div class="tweet">resume template<a>HTTP://lnk.to/m8tqzp</a><time>July 01, 2014 07:56:37</time></div>
    </div>
    <div class="footer-col abs" style="left:405px">
      <h3><svg viewBox="0 0 11 11"><rect x="1" y="1" width="9" height="9" fill="#e8363b"/></svg>Photo Feed</h3>
      <div class="photo-grid" role="img" aria-label="Six small concert and musician photo thumbnails">
        <span></span><span></span><span></span><span></span><span></span><span></span>
      </div>
    </div>
    <div class="footer-col abs" style="left:550px;width:140px;height:120px">
      <h3><svg viewBox="0 0 11 11"><rect x="0" y="2" width="11" height="8" fill="#e8363b"/><path d="M0 2 L5.5 6.5 L11 2" stroke="#1e1e1e" fill="none"/></svg>Newsletter Signup</h3>
      <div class="email-field">Enter your email address</div>
      <div class="socials"><span></span><span></span><span></span></div>
      <div class="btn-submit abs">Submit</div>
    </div>
  </footer>

  <section class="contact-band abs">
    <h2>MOSS LANTERN</h2>
    <div class="contact-line abs">
      <svg viewBox="0 0 11 12"><path d="M5.5 0C2.5 0 1 2 1 4.3 1 7 5.5 12 5.5 12S10 7 10 4.3C10 2 8.5 0 5.5 0z" fill="#f26a35"/><circle cx="5.5" cy="4.3" r="1.6" fill="#050505"/></svg>
      <span>18 Larkfield Lane, London, NW7 2QE</span><span>|</span>
      <svg viewBox="0 0 11 12"><path d="M2 0.5 4 0 5 3 3.5 4.3C4.2 6 5.5 7.5 7 8.3L8.5 7 11 8.5 10.4 10.5C9.5 12 5 11 2.5 7 0.5 4 .5 1.5 2 .5z" fill="#f26a35"/></svg>
      <span>0800.555.0192</span><span style="margin-left:8px">|</span>
      <svg viewBox="0 0 11 12" style="width:13px"><rect x="0" y="2" width="11" height="8" fill="#f26a35"/><path d="M0 2 L5.5 6.5 L11 2" stroke="#050505" fill="none"/></svg>
      <span style="margin-left:-5px">contact@mosslantern.com</span>
    </div>
  </section>

  <div class="legal abs">
    <span class="legal-copy abs">© Copyright 2014 Moss Lantern. All rights reserved.</span>
    <span class="legal-links abs">Privacy Policy &nbsp;|&nbsp; Term &amp; Conditions</span>
  </div>

</div>
</body>
</html>
```